Flyer Design Project - QRV Journeys

I am independent travel consultant. I started my business three weeks ago. I am utilizing social media, and email blasts. Additionally, I'd like to send flyers announcing my business. I want the attached logo recreated without Remote Desk Helpers on there. I'd like it to read QRV Journeys. I want the flyer to mention my Facebook page, www.friendloop.example/QRV-Journeys-8817602934150276/. Also, a beautiful picture that can spark the reader's interest to book travel. I also reserve rental cars, tickets for sporting events, concerts, etc., and tours. I can do rail tickets.
18 - 75 male and females

```html
<!DOCTYPE html>
<html lang="en">
<head>
<meta charset="UTF-8">
<title>QRV Journeys – Flyer</title>
<link rel="stylesheet" href="https://fonts.googleapis.com/css2?family=Catamaran:wght@700;800&family=Open+Sans:wght@600&family=Roboto:ital,wght@0,300;0,500;1,400&display=swap">
<style>
  :root {
    --orange: #fc5a06;
    --sky: #3dc3ef;
    --mustard: #e0b404;
    --white: #ffffff;
    --ink: #1e1e1e;
    --footer: #25282b;
    --lagoon-top: #3f8fd6;
    --lagoon-mid: #3f8a3c;
    --lagoon-low: #2fb7c9;
  }
  * { margin: 0; padding: 0; box-sizing: border-box; }
  html, body { width: 854px; height: 1200px; overflow: hidden; background: var(--white); }
  .flyer { position: relative; width: 854px; height: 1200px; overflow: hidden; background: var(--white); }

  .scene-photo {
    position: absolute; left: 0; top: 0; width: 854px; height: 560px;
    background: linear-gradient(180deg, var(--lagoon-top) 0%, #7fb6e6 14%, var(--lagoon-mid) 28%, #2f6e2e 45%, #4fc0d2 58%, var(--lagoon-low) 100%);
  }
  .brand {
    position: absolute; left: 52px; top: 78px;
    font-family: "Roboto", sans-serif; font-weight: 300; font-size: 82px;
    letter-spacing: 4px; color: var(--white); line-height: 1;
  }
  .snapshot {
    position: absolute; background: var(--white); border-radius: 10px; padding: 10px;
    box-shadow: 0 4px 14px rgba(0,0,0,0.35);
  }
  .snapshot .fill { width: 100%; height: 100%; border-radius: 4px; }
  .snapshot--one { left: 58px; top: 245px; width: 200px; height: 200px; transform: rotate(28deg); }
  .snapshot--one .fill { background: linear-gradient(160deg, #a9b6a8, #6a8f55 55%, #8a6a4a); }
  .snapshot--two { left: 250px; top: 228px; width: 260px; height: 215px; transform: rotate(28deg); }
  .snapshot--two .fill { background: linear-gradient(160deg, #dfe6e8, #7f9a6e 50%, #4c6a3f); }

  .service-bands { position: absolute; left: 0; top: 0; width: 854px; height: 1200px; }

  .service { position: absolute; text-align: center; color: var(--white); font-family: "Roboto", sans-serif; }
  .service__title { font-weight: 500; font-size: 24px; letter-spacing: 0.3px; }
  .service__note { font-style: italic; font-weight: 400; font-size: 15px; line-height: 22px; margin-top: 4px; }
  .service--tickets { left: 17px; width: 240px; top: 714px; }
  .service--cars { left: 297px; width: 260px; top: 637px; }
  .service--rail { left: 597px; width: 240px; top: 571px; }

  .pitch { position: absolute; left: 0; width: 854px; text-align: center; }
  .pitch__lead { top: 880px; font-family: "Catamaran", sans-serif; font-weight: 700; font-size: 28px; color: var(--orange); letter-spacing: 0.2px; }
  .pitch__name { top: 915px; font-family: "Catamaran", sans-serif; font-weight: 800; font-size: 74px; line-height: 1; color: var(--sky); letter-spacing: -1px; }
  .contact { top: 1016px; font-family: "Open Sans", sans-serif; font-weight: 600; font-size: 17px; line-height: 31px; color: var(--ink); letter-spacing: 0.2px; }

  .footer {
    position: absolute; left: 0; top: 1116px; width: 854px; height: 84px; background: var(--footer);
    display: flex; align-items: center; justify-content: center; gap: 18px;
    font-family: "Open Sans", sans-serif; font-weight: 600; font-size: 17px; color: var(--white);
  }
  .footer__dot { width: 30px; height: 30px; border-radius: 50%; background: var(--white); }
</style>
</head>
<body>
<div class="flyer">
  <div class="scene-photo" role="img" aria-label="Tropical lagoon with turquoise water, green mountains, a thatched roof and red flowers"></div>

  <div class="brand">QRV</div>

  <div class="snapshot snapshot--one"><div class="fill" role="img" aria-label="Snapshot of a traveller resting on a rocky desert trail"></div></div>
  <div class="snapshot snapshot--two"><div class="fill" role="img" aria-label="Snapshot of two friends raising their arms above a green valley"></div></div>

  <svg class="service-bands" viewBox="0 0 854 1200" xmlns="http://www.w3.org/2000/svg">
    <polygon points="0,553 284,480 284,814 0,887" fill="var(--orange)"/>
    <polygon points="284,480 569,411 569,745 284,814" fill="var(--sky)"/>
    <polygon points="569,411 854,347 854,682 569,745" fill="var(--mustard)"/>

    <!-- ticket icon -->
    <g transform="translate(137 630) rotate(-45)" fill="none" stroke="var(--white)">
      <path d="M-58,-30 H58 V-12 A12,12 0 0 0 58,12 V30 H-58 V12 A12,12 0 0 0 -58,-12 Z" fill="var(--white)" stroke="none"/>
      <rect x="-38" y="-16" width="76" height="32" fill="var(--orange)"/>
      <rect x="-30" y="-9" width="60" height="18" fill="var(--white)"/>
    </g>

    <!-- car icon -->
    <g transform="translate(427 557)" fill="var(--white)">
      <path d="M-40,-10 L-28,-40 Q-25,-46 -18,-46 H18 Q25,-46 28,-40 L40,-10 Q51,-8 51,4 V28 H-51 V4 Q-51,-8 -40,-10 Z"/>
      <rect x="-47" y="26" width="18" height="16" rx="3"/>
      <rect x="29" y="26" width="18" height="16" rx="3"/>
      <path d="M-26,-12 L-18,-36 H18 L26,-12 Z" fill="var(--sky)"/>
      <rect x="-20" y="4" width="40" height="5" rx="2" fill="var(--sky)"/>
      <circle cx="-36" cy="7" r="6" fill="var(--sky)"/>
      <circle cx="36" cy="7" r="6" fill="var(--sky)"/>
    </g>

    <!-- train icon -->
    <g transform="translate(717 476)" fill="var(--white)">
      <rect x="-42" y="-60" width="84" height="100" rx="22"/>
      <rect x="-32" y="-36" width="24" height="24" fill="var(--mustard)"/>
      <rect x="8" y="-36" width="24" height="24" fill="var(--mustard)"/>
      <rect x="-12" y="-50" width="24" height="7" rx="2" fill="var(--mustard)"/>
      <path d="M-34,-2 L0,14 L34,-2" fill="none" stroke="var(--mustard)" stroke-width="5"/>
      <circle cx="-24" cy="20" r="6" fill="var(--mustard)"/>
      <circle cx="24" cy="20" r="6" fill="var(--mustard)"/>
      <path d="M-30,40 L-42,62 M30,40 L42,62" stroke="var(--white)" stroke-width="5"/>
      <rect x="-36" y="48" width="72" height="5"/>
    </g>
  </svg>

  <div class="service service--tickets">
    <div class="service__title">EVENT TICKETS</div>
    <div class="service__note">Tickets for Sporting events,<br>Concerts, etc</div>
  </div>
  <div class="service service--cars">
    <div class="service__title">CAR RENTAL</div>
    <div class="service__note">Reserve rental cars</div>
  </div>
  <div class="service service--rail">
    <div class="service__title">RAIL BOOKING</div>
    <div class="service__note">Rail ticket booking also<br>done here!</div>
  </div>

  <div class="pitch pitch__lead">BOOK YOUR TRAVEL NEEDS WITH</div>
  <div class="pitch pitch__name">QRV JOURNEYS</div>
  <div class="pitch contact">(HOTEL, FLIGHTS, CRUISES AND RENTAL CARS) VIA QRV.TRIPDESKONLINE.EXAMPLE /<br>PHONE: (555) 014-3570 / EMAIL: HELLO@QRVJOURNEYS.EXAMPLE</div>

  <div class="footer">
    <span class="footer__dot"></span>
    <span>WWW.FRIENDLOOP.EXAMPLE/QRV-JOURNEYS-8817602934150276/</span>
  </div>
</div>
</body>
</html>
```